Hispanic Financial Counseling and Advocate Firm seeks business card design

Looking for a clean, professional business card design. This is a firm that specializes in providing financial education, coaching, and planning to the Hispanic community. The name of the company is Valemar, which means to prosper. We need a design that is clean, professional, and invokes trust, professionalism, but also welcoming. Our logo is a plant growing from a hand to give the messaging of of being in control of growing your financial future and security. Its part of a larger organization names Celesta Financial Group, who's logo is a tree with multi colored branches. We have the back of the card designed so we just need the front designed. the back is blue, so front needs to be a different background color, not blue.

Target Market(s)

Hispanic Community looking to better their future

Industry/Entity Type

financial services

Contact Information for Business Card

contact info: Anselmo Ibarra Jr, 951-555-0147, info@celestafinancialgroup.example. Celestafinancialgroup.example. tag line: Para un futuro mas seguro!

Requirements
Must have
• basics: logo, contact info.
Nice to have
• possibly incorporate the tree logo provided somehow
Should not have
• should not look like the back, needs to be different from the back provided.

```html
<!DOCTYPE html>
<html lang="es">
<head>
<meta charset="utf-8">
<title>Valemar · Tarjetas de presentación</title>
<link rel="stylesheet" href="https://fonts.googleapis.com/css2?family=Montserrat:wght@400;500;600;700&display=swap">
<style>
  :root {
    --stage: #cfcfcf;
    --navy-deep: #022a42;
    --navy-light: #0f3d56;
    --white: #ffffff;
    --green: #6aa72f;
    --green-light: #8fd24f;
    --slate: #46506d;
    --leaf-green: #8ac832;
    --leaf-blue: #1b9fd8;
    --leaf-red: #ea4a4f;
    --leaf-purple: #a98bd0;
    --leaf-yellow: #f5b819;
  }
  * { box-sizing: border-box; margin: 0; padding: 0; }
  html, body { width: 1200px; height: 1200px; overflow: hidden; }
  body {
    background: var(--stage);
    font-family: "Montserrat", sans-serif;
    position: relative;
  }
  .card {
    position: absolute;
    left: 180px;
    width: 840px;
    height: 480px;
    border-radius: 34px;
    overflow: hidden;
  }

  /* Back card */
  .card-back {
    top: 90px;
    background: radial-gradient(ellipse at 55% 50%, var(--navy-light), var(--navy-deep) 70%);
    color: var(--white);
  }
  .brand-lockup {
    position: absolute;
    left: 140px;
    top: 120px;
    display: flex;
    align-items: center;
    gap: 34px;
  }
  .brand-dot {
    width: 130px;
    height: 130px;
    border-radius: 50%;
    background: var(--white);
    opacity: .92;
  }
  .brand-divider {
    width: 2px;
    height: 170px;
    background: rgba(255,255,255,.75);
  }
  .brand-name {
    font-size: 46px;
    font-weight: 600;
    line-height: 1.1;
    letter-spacing: .5px;
  }
  .service-list {
    position: absolute;
    left: 250px;
    top: 345px;
    width: 460px;
    list-style: none;
    display: flex;
    flex-wrap: wrap;
    gap: 6px 18px;
    font-size: 19px;
    font-weight: 500;
  }
  .service-list li { display: flex; align-items: center; gap: 7px; }
  .service-list li::before {
    content: "";
    width: 9px; height: 14px;
    border-radius: 50% 50% 50% 50% / 70% 70% 30% 30%;
    background: var(--bullet);
  }

  /* Front card */
  .card-front {
    top: 630px;
    background: var(--white);
  }
  .front-swoosh { position: absolute; inset: 0; }
  .front-brand {
    position: absolute;
    left: 110px;
    top: 100px;
    width: 400px;
  }
  .front-name-row { display: flex; align-items: center; gap: 16px; }
  .front-dot {
    width: 50px; height: 50px;
    border-radius: 50%;
    background: var(--green);
  }
  .front-name {
    font-size: 68px;
    font-weight: 600;
    color: var(--green);
    line-height: 1;
  }
  .front-sub {
    margin-top: 14px;
    font-size: 18px;
    font-weight: 700;
    letter-spacing: 3px;
    color: var(--slate);
  }
  .front-tagline {
    margin-top: 6px;
    font-size: 21px;
    font-weight: 600;
    color: var(--green);
  }
  .holder-name {
    position: absolute;
    left: 60px;
    bottom: 40px;
    font-size: 26px;
    font-weight: 500;
    letter-spacing: 1.5px;
    color: var(--white);
  }
  .contact-list {
    position: absolute;
    left: 495px;
    top: 300px;
    list-style: none;
    color: var(--white);
    font-size: 15px;
    font-weight: 500;
    white-space: nowrap;
  }
  .contact-list li { display: flex; align-items: center; gap: 9px; margin-bottom: 8px; }
  .contact-list svg { width: 17px; height: 17px; flex: none; }
</style>
</head>
<body>

<section class="card card-back" aria-label="Reverso de la tarjeta">
  <div class="brand-lockup">
    <span class="brand-dot"></span>
    <span class="brand-divider"></span>
    <h1 class="brand-name">Celesta<br>Financial Group Inc</h1>
  </div>
  <ul class="service-list">
    <li style="--bullet: var(--leaf-green)">Inmigración</li>
    <li style="--bullet: var(--leaf-blue)">Planificacion Financiera</li>
    <li style="--bullet: var(--leaf-red)">Seguros</li>
    <li style="--bullet: var(--leaf-purple)">Impuestos</li>
    <li style="--bullet: var(--leaf-red)">Y mas</li>
    <li style="--bullet: var(--leaf-yellow)">Preparación de documentos</li>
  </ul>
</section>

<section class="card card-front" aria-label="Frente de la tarjeta">
  <svg class="front-swoosh" viewBox="0 0 840 480" preserveAspectRatio="none" aria-hidden="true">
    <path d="M0,392 Q560,350 735,0 L840,0 L840,480 L0,480Z" fill="var(--green-light)"/>
    <path d="M0,404 Q590,370 770,0 L840,0 L840,480 L0,480Z" fill="var(--green)"/>
  </svg>

  <div class="front-brand">
    <div class="front-name-row">
      <span class="front-dot"></span>
      <h2 class="front-name">Valemar</h2>
    </div>
    <p class="front-sub">SERVICIOS FINANCIEROS</p>
    <p class="front-tagline">Para un futuro mas seguro!</p>
  </div>

  <ul class="contact-list">
    <li>
      <svg viewBox="0 0 24 24"><path fill="currentColor" d="M6.6 10.8a15 15 0 0 0 6.6 6.6l2.2-2.2c.3-.3.7-.4 1-.2 1.1.4 2.3.6 3.6.6.6 0 1 .4 1 1V20c0 .6-.4 1-1 1A17 17 0 0 1 3 4c0-.6.4-1 1-1h3.5c.6 0 1 .4 1 1 0 1.3.2 2.5.6 3.6.1.3 0 .7-.2 1z"/></svg>
      951-555-0147
    </li>
    <li>
      <svg viewBox="0 0 24 24"><rect x="2" y="5" width="20" height="14" rx="1" fill="none" stroke="currentColor" stroke-width="2"/><path d="M2 6l10 7 10-7" fill="none" stroke="currentColor" stroke-width="2"/></svg>
      info@celestafinancialgroup.example
    </li>
    <li>
      <svg viewBox="0 0 24 24" fill="none" stroke="currentColor" stroke-width="1.8"><circle cx="12" cy="12" r="9.5"/><ellipse cx="12" cy="12" rx="4" ry="9.5"/><path d="M2.5 12h19M4 7h16M4 17h16"/></svg>
      Celestafinancialgroup.example
    </li>
  </ul>

  <p class="holder-name">ANSELMO IBARRA JR</p>
</section>

</body>
</html>
```